Luxury Brand Real Estate For Sale sign

**Update** I've added some examples from the internet of other signs that have a look similar to what I would like to see. I do not want my personal name in the sign. And the word FOR SALE Does not need to be so large - it can be more subtle.
I want to create a Real Estate for sale sign for my company that will be used for luxury/higher end real estate listings. I’m sharing my business card as well as a logo with new teal color to show what we're moving towards: we’re using Teal, white, black and gold.
Hoping the sign is simple, sophisticated and eye catching.
The sign should be 24" wide by 30" tall including the company name: Harbor Crest Realty Group and our logo, office phone number 727-555-0148 and website www.hcrgproperty.example the words "For Sale"
Optional to add this e-mail address info@hcrgproperty.example to the sign
Luxury home buyers
Real Estate

```html
<!DOCTYPE html>
<html lang="en">
<head>
<meta charset="utf-8">
<title>Harbor Crest Realty Group – For Sale Sign</title>
<link rel="stylesheet" href="https://fonts.googleapis.com/css2?family=Oswald:wght@300&family=Roboto+Condensed:wght@700&family=Poppins:wght@400;600&display=swap">
<style>
  :root {
    --backdrop: #f6f6f6;
    --sign-charcoal: #4b4c4e;
    --brand-teal: #148482;
    --text-white: #ffffff;
    --gold-deep: #f5c834;
    --gold-light: #fff4cf;
  }
  html, body {
    margin: 0;
    padding: 0;
    width: 1200px;
    height: 1200px;
    overflow: hidden;
    background: var(--backdrop);
  }
  .canvas {
    display: block;
    width: 1200px;
    height: 1200px;
  }
  .sign-panel { fill: var(--sign-charcoal); filter: drop-shadow(0 6px 10px rgba(0,0,0,0.25)); }
  .gold-frame { fill: none; stroke: url(#goldSheen); stroke-width: 5; }
  .headline-band { fill: var(--brand-teal); }
  .headline {
    font-family: "Oswald", "Arial Narrow", sans-serif;
    font-weight: 300;
    font-size: 232px;
    fill: var(--text-white);
  }
  .phone {
    font-family: "Roboto Condensed", "Arial Narrow", sans-serif;
    font-weight: 700;
    font-size: 152px;
    fill: var(--text-white);
  }
  .website {
    font-family: "Poppins", Arial, sans-serif;
    font-weight: 400;
    font-size: 54px;
    fill: var(--text-white);
  }
  .brand-plate { fill: var(--text-white); }
  .brand-square { fill: var(--brand-teal); }
  .brand-name {
    font-family: "Poppins", Arial, sans-serif;
    font-weight: 600;
    font-size: 36px;
    fill: var(--brand-teal);
  }
</style>
</head>
<body>
<svg class="canvas" viewBox="0 0 1200 1200" xmlns="http://www.w3.org/2000/svg">
  <defs>
    <linearGradient id="goldSheen" x1="0" y1="0" x2="1" y2="1">
      <stop offset="0" stop-color="var(--gold-deep)"/>
      <stop offset="0.5" stop-color="var(--gold-light)"/>
      <stop offset="1" stop-color="var(--gold-deep)"/>
    </linearGradient>
  </defs>

  <rect class="sign-panel" x="167" y="60" width="865" height="1075"/>
  <rect class="gold-frame" x="200" y="95" width="798" height="1010"/>

  <rect class="headline-band" x="167" y="137" width="865" height="326"/>
  <text class="headline" x="233" y="394" textLength="737" lengthAdjust="spacingAndGlyphs">FOR SALE</text>

  <text class="phone" x="228" y="657" textLength="738" lengthAdjust="spacingAndGlyphs">727-555-0148</text>

  <text class="website" x="229" y="780" textLength="740" lengthAdjust="spacing">www.hcrgproperty.example</text>

  <rect class="brand-plate" x="237" y="865" width="723" height="191"/>
  <rect class="brand-square" x="290" y="938" width="44" height="44"/>
  <text class="brand-name" x="356" y="973" textLength="560" lengthAdjust="spacing">Harbor Crest Realty Group</text>
</svg>
</body>
</html>
```